New Brava Tiles Billboard at HQ

Looking to design a catchy image / theme for a billboard located just above our corporate HQ showroom and warehouse, along the service road of a 6-lane highway. Billboard measures 8ft x 24 ft. Would like to highlight that the store location is directly beneath the sign.

We are a retail and wholesale business selling premium flooring, ready to assemble cabinets, and granite countertops. See image ideas attached. Our information:
NAME: Brava Tiles, Cabinets, Countertops
ADDRESS: 412 W. Hwy 29, Duncanville, TX 75990
WEBSITE: www.bravatiles-example.com
PHONE: 555-8-DECKED (555-833-2533)

```html
<!DOCTYPE html>
<html lang="en">
<head>
<meta charset="utf-8">
<title>Brava Tiles Billboard</title>
<link href="https://fonts.googleapis.com/css2?family=Anton&family=Montserrat:wght@600;700;800&display=swap" rel="stylesheet">
<style>
  :root {
    --page: #ffffff;
    --panel-white: #ffffff;
    --brand-green: #7cc242;
    --green-light: #8fd14f;
    --green-dark: #5fa82c;
    --ink: #111111;
    --ink-soft: #1c1c1c;
    --white: #ffffff;
  }
  * { box-sizing: border-box; margin: 0; padding: 0; }
  html, body {
    width: 800px; height: 1200px; overflow: hidden;
    background: var(--page);
  }
  .canvas { position: relative; width: 800px; height: 1200px; }

  .billboard {
    position: absolute; left: 20px; top: 473px;
    width: 760px; height: 254px;
    display: flex;
    box-shadow: 0 2px 6px rgba(0,0,0,0.35);
  }

  /* left: brand + address */
  .brand-panel {
    width: 360px; height: 100%;
    background: var(--panel-white);
    position: relative;
    padding: 0 22px;
  }
  .brand-name {
    position: absolute; left: 24px; top: 58px;
    display: flex; align-items: center; gap: 12px;
    font-family: "Montserrat", sans-serif;
    font-weight: 800; font-size: 44px; line-height: 1;
    color: var(--ink);
    letter-spacing: -0.5px;
  }
  .brand-mark {
    width: 34px; height: 34px; background: var(--brand-green); flex: none;
  }
  .address {
    position: absolute; left: 24px; top: 176px;
    display: flex; gap: 8px;
    font-family: "Montserrat", sans-serif;
    font-weight: 700; font-size: 21px; line-height: 1.3;
    color: var(--ink);
  }
  .address .pin { width: 14px; height: 20px; margin-top: 6px; flex: none; }

  /* right: offer panel */
  .offer-panel {
    position: relative; flex: 1; height: 100%;
    overflow: hidden;
  }
  .plank-texture {
    position: absolute; inset: 0;
    background: linear-gradient(135deg, var(--green-light), var(--brand-green) 55%, var(--green-dark));
  }
  .offer-content { position: absolute; inset: 0; padding-left: 32px; }
  .services {
    position: absolute; left: 32px; top: 14px;
    font-family: "Montserrat", sans-serif;
    font-weight: 700; font-size: 13.5px; letter-spacing: 0.4px;
    color: var(--ink-soft); text-transform: uppercase;
  }
  .headline {
    position: absolute; left: 32px; top: 36px;
    font-family: "Anton", sans-serif;
    font-size: 50px; line-height: 0.98;
    color: var(--white); text-transform: uppercase;
    text-shadow: 2px 2px 2px rgba(0,0,0,0.35);
    letter-spacing: 0.5px;
  }
  .website {
    position: absolute; left: 32px; top: 150px;
    display: flex; align-items: center; gap: 10px;
    font-family: "Montserrat", sans-serif;
    font-weight: 700; font-size: 19.5px;
    color: var(--ink);
  }
  .website .globe { width: 14px; height: 14px; }

  .phone-band {
    position: absolute; left: 0; top: 190px; width: 390px; height: 44px;
  }
  .phone-band svg.arrow { position: absolute; inset: 0; }
  .phone {
    position: absolute; left: 14px; top: 0; height: 44px;
    display: flex; align-items: center; gap: 8px;
    font-family: "Anton", sans-serif;
    font-size: 22px; color: var(--ink-soft);
  }
  .phone .phone-icon { width: 20px; height: 20px; }
</style>
</head>
<body>
<div class="canvas">
  <section class="billboard" aria-label="Brava Tiles billboard">
    <div class="brand-panel">
      <div class="brand-name"><span class="brand-mark"></span>Brava Tiles</div>
      <p class="address">
        <svg class="pin" viewBox="0 0 14 20" aria-hidden="true">
          <path d="M7 0a7 7 0 0 0-7 7c0 5 7 13 7 13s7-8 7-13a7 7 0 0 0-7-7z" fill="#111"/>
          <circle cx="7" cy="7" r="2.6" fill="#fff"/>
        </svg>
        <span>412 W. Hwy 29,<br>Duncanville, TX 75990</span>
      </p>
    </div>

    <div class="offer-panel">
      <div class="plank-texture" role="img" aria-label="Green painted wood plank texture"></div>
      <div class="offer-content">
        <p class="services">Brava Tiles, Cabinets, Countertops</p>
        <h1 class="headline">Need<br>Flooring?</h1>
        <p class="website">
          <svg class="globe" viewBox="0 0 14 14" aria-hidden="true">
            <circle cx="7" cy="7" r="6" fill="none" stroke="#222" stroke-width="1.3"/>
            <ellipse cx="7" cy="7" rx="2.6" ry="6" fill="none" stroke="#222" stroke-width="1"/>
            <line x1="1" y1="7" x2="13" y2="7" stroke="#222" stroke-width="1"/>
          </svg>
          www.bravatiles-example.com
        </p>
        <div class="phone-band">
          <svg class="arrow" viewBox="0 0 390 44" preserveAspectRatio="none" aria-hidden="true">
            <path d="M0 3 H352 V-2 L386 22 L352 46 V41 H0" fill="rgba(255,255,255,0.12)" stroke="#fff" stroke-width="3"/>
          </svg>
          <p class="phone">
            <svg class="phone-icon" viewBox="0 0 20 20" aria-hidden="true">
              <circle cx="10" cy="10" r="9.5" fill="#fff"/>
              <path d="M6.5 5.2l2 2-1 1.4a7 7 0 0 0 3.9 3.9l1.4-1 2 2-1.2 1.5C10 15 5 10 5.1 6.4z" fill="#7cc242"/>
            </svg>
            555-8-DECKED (555-833-2533)
          </p>
        </div>
      </div>
    </div>
  </section>
</div>
</body>
</html>
```